KRANO study results infographic

We enjoyed the previous infographic design you provided for us (The GaRVU cohort study Infographic), and would like to invite you to design another infographic in a similar style and layout.
We need an infographic which presents the results from the KRANO research trial. It should be colourful and engaging, in understandable language and showing the steps to get to the results. This is to showcase the results to patients/the public/clinicians, giving a brief summary of what the study proved. The final design should have the KRANO logo at the top (please see attached and https://krano.pelbu.quenmarsh.example/welcome-krano-trial)
I have attached the required logos which need to be used (KRANO, Penhallow Injury and Acute Care, University of Castlemere) as well as an example from another study, The GaRVU cohort study Infographic, as an example of what the layout could look like. Please DO NOT use the content from the The GaRVU cohort study Infographic example though, please instead use the content from the attached document 'KRANO_InfographicDesignInformation_Plinthwork'.

```html
<!DOCTYPE html>
<html lang="en">
<head>
<meta charset="utf-8">
<title>KRANO study results infographic</title>
<link rel="stylesheet" href="https://fonts.googleapis.com/css2?family=Poppins:wght@400;500;600;700;800&display=swap">
<style>
:root{
  --navy:#1f365f;
  --navy-deep:#1a2f55;
  --blue:#2a9fdc;
  --blue-soft:#bfe0f4;
  --pale:#eaf4fb;
  --ink:#1b2a4a;
  --white:#ffffff;
}
*{margin:0;padding:0;box-sizing:border-box}
html,body{width:1200px;height:2792px;overflow:hidden}
body{font-family:'Poppins',sans-serif;color:var(--ink);background:var(--white);position:relative}
.abs{position:absolute}
.header-shape{left:0;top:0;width:1200px;height:410px}
.brand{left:0;width:1200px;top:62px;text-align:center;font-weight:800;font-size:56px;color:var(--white);letter-spacing:4px}
.brand-dot{display:inline-block;width:22px;height:22px;border-radius:50%;background:var(--blue);margin-right:14px;vertical-align:middle}
.title{left:60px;width:1080px;top:188px;text-align:center;color:var(--white);font-weight:800;font-size:28.5px;line-height:29px;text-transform:uppercase}
.title .accent{color:var(--blue)}
.intro-heading{left:68px;top:428px;width:560px;font-weight:800;font-size:31px;line-height:39px;color:var(--navy);text-transform:uppercase}
.intro-heading .sub{display:block;color:var(--blue);font-weight:500}
.intro-text{left:70px;top:608px;width:540px;border-left:4px solid var(--blue);padding-left:22px;font-size:18.5px;line-height:29px}
.intro-art{left:629px;top:434px;width:527px;height:406px;border-radius:50% 50% 40% 40%;background:linear-gradient(160deg,#eaf3fb,#cfe4f4)}
.findings-band{left:0;top:900px;width:1200px;height:1203px;background:linear-gradient(180deg,#e2eff9 0%,#eef6fc 30%,#f1f7fc 100%)}
.section-title{font-weight:800;color:var(--blue);text-transform:uppercase;letter-spacing:1px}
.findings-title{left:0;width:1200px;top:938px;text-align:center;font-size:38px}
.timeline{left:183px;top:1061px;width:850px;border-top:2px dashed #9cc6e6}
.tl-dot{width:10px;height:10px;border-radius:50%;background:var(--blue);top:1057px}
.finding-icon{width:108px;height:108px;border-radius:50%;background:var(--white);border:4px solid var(--blue);top:1003px;display:flex;align-items:center;justify-content:center;box-shadow:0 6px 14px rgba(42,159,220,.18)}
.finding-text{width:250px;text-align:center;font-weight:700;font-size:17px;line-height:26px;color:var(--navy)}
.card{left:89px;top:1279px;width:1052px;height:342px;background:var(--white);border-bottom:4px solid var(--blue)}
.card-art{left:163px;top:1317px;width:265px;height:266px;border-radius:50%;border:2px dashed #b7d9ef;background:linear-gradient(160deg,#f3f8fc,#dcecf7)}
.card-heading{left:476px;top:1355px;font-weight:800;font-size:33px;color:var(--navy);letter-spacing:.5px}
.card-text{left:478px;top:1407px;width:610px;border-left:4px solid var(--blue);padding-left:20px;font-size:21px;line-height:29px}
.card-text strong{color:var(--blue);font-weight:700}
.details-title{left:108px;top:1666px;font-size:33px}
.detail{display:flex;align-items:flex-start;font-size:21px;line-height:29px;width:480px}
.chev{flex:0 0 35px;width:35px;height:35px;border-radius:50%;background:var(--blue);margin-right:12px;display:flex;align-items:center;justify-content:center}
.audience-title{left:0;width:1200px;top:2138px;text-align:center;font-size:29px}
.aud{width:196px;height:196px;border-radius:50%;border:2px dashed #a8d2ee;top:2195px;background:var(--white)}
.aud-icon{position:absolute;left:61px;top:26px;width:74px;height:74px;border-radius:50%;display:flex;align-items:center;justify-content:center}
.aud-label{position:absolute;left:10px;width:172px;top:112px;text-align:center;font-weight:700;font-size:16px;line-height:21px;color:var(--navy)}
.uni{left:109px;top:2464px;width:200px;height:200px;border-radius:50%;background:var(--navy);display:flex;align-items:center;justify-content:center;text-align:center;color:var(--white);font-weight:500;font-size:19px;line-height:25px;padding:20px}
.sponsor-title{left:364px;top:2478px;font-size:26px}
.sponsor-text{left:364px;top:2517px;width:680px;font-weight:700;font-size:19.5px;line-height:29px;color:var(--navy)}
.partner{left:366px;top:2628px;display:flex;align-items:center;font-weight:500;font-size:21px;color:#6b6f78}
.partner-mark{width:26px;height:26px;background:#6b6f78;margin-right:10px}
.footer{left:0;top:2699px;width:1200px;height:93px;background:var(--navy);display:flex;align-items:center;justify-content:center;color:var(--white);font-size:20px}
.footer strong{font-weight:700}
.mail{width:36px;height:36px;border-radius:50%;background:var(--blue);margin:0 14px 0 48px;display:flex;align-items:center;justify-content:center}
</style>
</head>
<body>

<svg class="abs header-shape" viewBox="0 0 1200 410" aria-hidden="true">
  <polygon points="0,0 1200,0 1200,290 600,410 0,290" fill="#2a9fdc"/>
  <polygon points="0,0 1200,0 1200,280 600,398 0,280" fill="#1f365f"/>
</svg>
<div class="abs brand"><span class="brand-dot"></span>KRANO</div>
<h1 class="abs title">A feasibility study of standard dressings versus<br>negative-pressure wound therapy in the treatment of<br>adult patients having surgical incisions for hip fractures:<br><span class="accent">The KRANO randomized controlled trial</span></h1>

<h2 class="abs intro-heading">Hip fracture surgery: can<br>‘vacuum’ dressings<br>reduce deep infections?<span class="sub">(Feasibility trial)</span></h2>
<p class="abs intro-text">Adults &gt;65 years undergoing hip fracture surgery at 5 UK centres were randomised to standard dressings or negative pressure ‘vacuum’ dressings (called iNPWT). Deep infection (CDC-defined) was assessed at 30 &amp; 90 days; other outcomes like Health Related Quality of Life were assessed at 120 days. The overall deep SSI rate was ~4%; effect signals favoured iNPWT, and a definitive trial was deemed feasible.</p>
<div class="abs intro-art" role="img" aria-label="Illustration of a clinician with a tablet beside a pelvis diagram and an older patient in a wheelchair"></div>

<div class="abs findings-band"></div>
<h2 class="abs section-title findings-title">Findings</h2>
<div class="abs timeline"></div>
<div class="abs tl-dot" style="left:316px"></div>
<div class="abs tl-dot" style="left:607px"></div>
<div class="abs tl-dot" style="left:892px"></div>

<div class="abs finding-icon" style="left:129px">
  <svg width="56" height="50" viewBox="0 0 56 50" fill="none" stroke="#1f365f" stroke-width="2.4"><circle cx="14" cy="10" r="6"/><circle cx="28" cy="8" r="6"/><circle cx="42" cy="10" r="6"/><path d="M4 36v-8a10 10 0 0 1 20 0M18 34v-8a10 10 0 0 1 20 0M32 36v-8a10 10 0 0 1 20 0"/><path d="M4 46v-8a10 10 0 0 1 48 0v8z"/></svg>
</div>
<div class="abs finding-icon" style="left:405px">
  <svg width="56" height="54" viewBox="0 0 56 54" fill="none" stroke="#1f365f" stroke-width="2.4"><rect x="3" y="7" width="44" height="40" rx="3"/><path d="M3 17h44M14 2v9M36 2v9"/><path d="M10 24h5M20 24h5M30 24h5M10 32h5M20 32h5M10 40h5M20 40h5"/><circle cx="42" cy="42" r="10" fill="#fff"/><path d="M42 36v6l4 3"/></svg>
</div>
<div class="abs finding-icon" style="left:697px">
  <svg width="50" height="56" viewBox="0 0 50 56" fill="none" stroke="#1f365f" stroke-width="2.4"><path d="M30 6a6 6 0 1 1 10 6l-20 28a6 6 0 1 1-8 6a6 6 0 1 1 6-8l20-28a6 6 0 0 1-8-4z"/><path d="M40 30l6-3M38 38l6 2M34 44l3 5"/></svg>
</div>
<div class="abs finding-icon" style="left:979px">
  <svg width="48" height="56" viewBox="0 0 48 56" fill="none" stroke="#1f365f" stroke-width="2.4"><rect x="4" y="6" width="40" height="47" rx="3"/><rect x="15" y="2" width="18" height="8" rx="2" fill="#fff"/><path d="M24 16v10M19 21h10M11 34h4M19 34h18M11 42h4M19 42h18"/></svg>
</div>

<p class="abs finding-text" style="left:55px;top:1117px">462 valid randomisations; recruitment rate ~62% of eligible cases.</p>
<p class="abs finding-text" style="left:306px;top:1141px;width:306px">Deep SSI at 30 days:<br>6.4% (standard) vs 1.9% (iNPWT) at 90 days: 6.4% vs 2.3%.</p>
<p class="abs finding-text" style="left:626px;top:1117px">Overall 30-day deep SSI 4.2% for hip fracture population</p>
<p class="abs finding-text" style="left:916px;top:1141px;width:240px">Feasibility confirmed for a fully powered effectiveness trial.</p>

<div class="abs card"></div>
<div class="abs card-art" role="img" aria-label="Illustration of an older person in a wheelchair beside an older person walking with a crutch"></div>
<h2 class="abs card-heading">ELIGIBILITY CRITERIA</h2>
<p class="abs card-text">Inclusion: age &gt;<strong>65 years</strong>; undergoing any surgery for hip fracture. Exclusion: undisplaced intracapsular fracture treated with cannulated screws; other factors precluding participation.</p>

<h2 class="abs section-title details-title">Study details</h2>
<div class="abs detail" style="left:108px;top:1742px"><span class="chev"><svg width="12" height="14" viewBox="0 0 12 14"><path d="M3 2l6 5-6 5" fill="none" stroke="#fff" stroke-width="2.6"/></svg></span><span>Design: Two-arm multicentre RCT embedded in the GaRVU cohort</span></div>
<div class="abs detail" style="left:108px;top:1829px"><span class="chev"><svg width="12" height="14" viewBox="0 0 12 14"><path d="M3 2l6 5-6 5" fill="none" stroke="#fff" stroke-width="2.6"/></svg></span><span>Sites: 5 UK centres</span></div>
<div class="abs detail" style="left:108px;top:1891px"><span class="chev"><svg width="12" height="14" viewBox="0 0 12 14"><path d="M3 2l6 5-6 5" fill="none" stroke="#fff" stroke-width="2.6"/></svg></span><span>Participants: 462 randomised</span></div>
<div class="abs detail" style="left:108px;top:1952px"><span class="chev"><svg width="12" height="14" viewBox="0 0 12 14"><path d="M3 2l6 5-6 5" fill="none" stroke="#fff" stroke-width="2.6"/></svg></span><span>Recruitment: Jul 2017–Feb 2018</span></div>

<div class="abs detail" style="left:650px;top:1737px"><span class="chev"><svg width="12" height="14" viewBox="0 0 12 14"><path d="M3 2l6 5-6 5" fill="none" stroke="#fff" stroke-width="2.6"/></svg></span><span>Follow-up to 120 days</span></div>
<div class="abs detail" style="left:650px;top:1797px"><span class="chev"><svg width="12" height="14" viewBox="0 0 12 14"><path d="M3 2l6 5-6 5" fill="none" stroke="#fff" stroke-width="2.6"/></svg></span><span>Primary outcome: deep SSI at 30 &amp; 90 days (CDC)</span></div>
<div class="abs detail" style="left:650px;top:1888px"><span class="chev"><svg width="12" height="14" viewBox="0 0 12 14"><path d="M3 2l6 5-6 5" fill="none" stroke="#fff" stroke-width="2.6"/></svg></span><span>Secondary: recruitment metrics, further surgery, EQ-5D-5L, complications, mobility, residential status</span></div>
<div class="abs detail" style="left:650px;top:2006px"><span class="chev"><svg width="12" height="14" viewBox="0 0 12 14"><path d="M3 2l6 5-6 5" fill="none" stroke="#fff" stroke-width="2.6"/></svg></span><span>Registration: ISRCTN48120593.</span></div>

<h2 class="abs section-title audience-title">Target audience</h2>
<div class="abs aud" style="left:87px"><div class="aud-icon" style="background:var(--blue)"><svg width="36" height="38" viewBox="0 0 36 38" fill="none" stroke="#fff" stroke-width="2.4"><circle cx="18" cy="10" r="7"/><path d="M3 37v-6a15 15 0 0 1 30 0v6z"/><path d="M8 14h4M10 12v4"/></svg></div><p class="aud-label">Orthopaedic &amp;<br>Trauma<br>Clinicians</p></div>
<div class="abs aud" style="left:298px"><div class="aud-icon" style="background:var(--navy)"><svg width="40" height="38" viewBox="0 0 40 38" fill="none" stroke="#fff" stroke-width="2.4"><circle cx="20" cy="7" r="5"/><circle cx="8" cy="12" r="4"/><circle cx="32" cy="12" r="4"/><path d="M12 36V22a8 8 0 0 1 16 0v14M2 34v-8a6 6 0 0 1 8-5M38 34v-8a6 6 0 0 0-8-5"/></svg></div><p class="aud-label">Orthogeriatric<br>Teams</p></div>
<div class="abs aud" style="left:507px"><div class="aud-icon" style="background:var(--blue)"><svg width="38" height="38" viewBox="0 0 38 38" fill="none" stroke="#fff" stroke-width="2.4"><path d="M6 32l16-16 4 4-16 16H6zM20 14l8-8 4 4-8 8M28 6l4-4 4 4-4 4"/><rect x="26" y="24" width="9" height="12" rx="2"/></svg></div><p class="aud-label">Infection<br>Prevention Leads</p></div>
<div class="abs aud" style="left:711px"><div class="aud-icon" style="background:var(--navy)"><svg width="36" height="38" viewBox="0 0 36 38" fill="none" stroke="#fff" stroke-width="2.4"><circle cx="18" cy="10" r="7"/><path d="M3 37v-6a15 15 0 0 1 30 0v6zM18 22l-3 5 3 8 3-8z"/></svg></div><p class="aud-label" style="top:120px">Commissioners</p></div>
<div class="abs aud" style="left:917px"><div class="aud-icon" style="background:var(--blue)"><svg width="40" height="38" viewBox="0 0 40 38" fill="none" stroke="#fff" stroke-width="2.4"><path d="M20 22l-8-8a5 5 0 0 1 8-6a5 5 0 0 1 8 6z"/><path d="M3 20l8 12h18l8-12"/></svg></div><p class="aud-label">Patient/Public<br>Audiences</p></div>

<div class="abs uni">University of Castlemere</div>
<h2 class="abs section-title sponsor-title">Sponsor</h2>
<p class="abs sponsor-text">Royal Guild of Surgical Practice/Harrowgate Medical Foundation (training fellowship), Castlemere Biomedical Research Centre (infrastructure support), Varden &amp; Holt (device supply).</p>
<div class="abs partner"><span class="partner-mark"></span>Penhallow Injury and Acute Care</div>

<footer class="abs footer">Chief Investigator:&nbsp;<strong>Elena Rudvik</strong><span class="mail"><svg width="18" height="14" viewBox="0 0 18 14" fill="none" stroke="#fff" stroke-width="1.8"><rect x="1" y="1" width="16" height="12" rx="1.5"/><path d="M1 2l8 6 8-6"/></svg></span><strong>elena.rudvik@krano-study.example</strong></footer>

</body>
</html>
```